Name Card, Stationary, Warranty Seal, Receipt Book
Qorvix Repair Centre
Simple
Tomas
27 Wexley Lane #08-04
Singapore 58817
qrv@qorvix-mail.test
www.qorvix-fix.test
State in we Repair veltra, Plumstone, Korvane and others Smart Phones
On the spot Repair.
For this you are able to use your creative base on our line of repair service

```html
<!DOCTYPE html>
<html lang="en">
<head>
<meta charset="utf-8">
<title>Qorvix Repair Centre – Name Card</title>
<link rel="stylesheet" href="https://fonts.googleapis.com/css2?family=Arimo:wght@400;700&display=swap">
<style>
  :root {
    --page-bg: #e9e6e2;
    --card-white: #ffffff;
    --red-deep: #e01f26;
    --red-mid: #ec3b22;
    --orange-glow: #f7a02c;
    --swoosh-blue: #27389a;
    --swoosh-light: #8f9bd6;
    --brand-orange: #f07519;
    --brand-mark: #9aa3ad;
    --text-light: #ffffff;
  }
  * { margin: 0; padding: 0; box-sizing: border-box; }
  html, body {
    width: 1200px; height: 780px; overflow: hidden;
    background: var(--page-bg);
    font-family: "Arimo", Arial, sans-serif;
  }
  .name-card {
    position: absolute; left: 80px; top: 80px;
    width: 1040px; height: 620px;
    border-radius: 36px; overflow: hidden;
    background: var(--card-white);
    box-shadow: 0 6px 22px rgba(0,0,0,0.18);
  }
  .card-art { position: absolute; inset: 0; }
  .holder-name {
    position: absolute; left: 64px; top: 58px;
    color: var(--text-light); font-weight: 700; font-size: 30px;
  }
  .address {
    position: absolute; left: 64px; top: 296px;
    color: var(--text-light); font-size: 20px; line-height: 28px;
  }
  .contact-list {
    position: absolute; left: 64px; top: 392px;
    list-style: none; color: var(--text-light); font-size: 20px;
  }
  .contact-list li {
    display: flex; align-items: center; gap: 16px; height: 34px;
  }
  .contact-list svg { width: 20px; height: 20px; flex: none; }
  .brand {
    position: absolute; left: 560px; top: 120px; width: 420px;
    display: flex; flex-direction: column; align-items: center;
  }
  .brand-dot {
    width: 110px; height: 110px; border-radius: 50%;
    background: var(--brand-mark); margin-bottom: 22px;
  }
  .brand-name {
    color: var(--brand-orange); font-weight: 700;
    font-size: 96px; line-height: 1; letter-spacing: 2px; text-transform: uppercase;
  }
  .brand-sub {
    color: var(--brand-orange); font-weight: 700;
    font-size: 34px; letter-spacing: 4px; text-transform: uppercase; margin-top: 6px;
  }
</style>
</head>
<body>
  <section class="name-card">
    <svg class="card-art" viewBox="0 0 1040 620" width="1040" height="620" aria-hidden="true">
      <defs>
        <radialGradient id="redPanel" cx="0.32" cy="0.5" r="0.75">
          <stop offset="0" stop-color="var(--orange-glow)"/>
          <stop offset="0.45" stop-color="var(--red-mid)"/>
          <stop offset="1" stop-color="var(--red-deep)"/>
        </radialGradient>
      </defs>
      <path d="M0 0 H430 C520 120 560 290 505 410 C470 490 430 560 405 620 H0 Z" fill="url(#redPanel)"/>
      <path d="M450 0 C545 120 585 290 528 412 C492 492 452 560 428 620"
            fill="none" stroke="var(--swoosh-light)" stroke-width="4"/>
      <path d="M436 0 C530 120 572 290 515 410 C480 490 440 560 415 620"
            fill="none" stroke="var(--swoosh-blue)" stroke-width="9"/>
    </svg>

    <h1 class="holder-name">Tomas</h1>

    <p class="address">27 Wexley Lane #08-04<br>Singapore 58817</p>

    <ul class="contact-list">
      <li>
        <svg viewBox="0 0 20 20"><path d="M5 2 L8 6 L6.5 8 C7.5 10.5 9.5 12.5 12 13.5 L14 12 L18 15 L16 18 C9 18 2 11 2 4 Z" fill="#fff"/></svg>
        84150627
      </li>
      <li>
        <svg viewBox="0 0 20 20"><rect x="5" y="2" width="10" height="6" fill="#fff"/><rect x="2" y="8" width="16" height="8" rx="2" fill="#fff"/><rect x="5" y="13" width="10" height="5" fill="#fff"/></svg>
        61092738
      </li>
      <li>
        <svg viewBox="0 0 20 20"><circle cx="10" cy="10" r="8" fill="none" stroke="#fff" stroke-width="2"/><circle cx="10" cy="10" r="3" fill="none" stroke="#fff" stroke-width="2"/><path d="M13 7 V12 Q13 14 15 13" fill="none" stroke="#fff" stroke-width="2"/></svg>
        qrv@qorvix-mail.test
      </li>
      <li>
        <svg viewBox="0 0 20 20"><circle cx="10" cy="10" r="8" fill="none" stroke="#fff" stroke-width="1.8"/><ellipse cx="10" cy="10" rx="3.5" ry="8" fill="none" stroke="#fff" stroke-width="1.5"/><path d="M2 10 H18" stroke="#fff" stroke-width="1.5"/></svg>
        www.qorvix-fix.test
      </li>
    </ul>

    <div class="brand">
      <div class="brand-dot"></div>
      <div class="brand-name">Qorvix</div>
      <div class="brand-sub">Repair Centre</div>
    </div>
  </section>
</body>
</html>
```